Cover page for Master's thesis (in Word)

I need a cover page for my Master's thesis which I am currently working on. The topic is "Mobile Usability" so MOBILE should also be the overall theme of the design. The primary color should be blue since my school and the company where I am writing my thesis are primarily using blue in their Corporate Identities.
I enclosed a template in Word and pdf with all the necessary information that must be included on the cover page. Please also consider and adhere to the page margins and the printable areas set in the Word template and please use Verdana for the mandatory text elements mentioned. The topic font can be different and it's up to you.
The design shouldn't be too fancy since this is a dissertation and not an ad for an Quince product. I would prefer a simple, flat, modern and professional design with flat colors. I also attached the logo of my University and my company (which should of course be included) as well as a leaflet of my Uni for inspiration.

If you have any questions or if you need more information or material, just drop me a line.

Thanks a lot in advance!
Torben

```html
<!DOCTYPE html>
<html lang="en">
<head>
<meta charset="utf-8">
<title>Master's Thesis Cover – Mobile Usability</title>
<link rel="stylesheet" href="https://fonts.googleapis.com/css2?family=Bebas+Neue&family=Barlow:wght@300;400;500&display=swap">
<style>
  :root {
    --brand-blue: #0b5592;
    --ink: #1c1c1c;
    --muted-grey: #6f6f6f;
    --paper: #ffffff;
  }
  html, body {
    margin: 0;
    padding: 0;
    overflow: hidden;
    background: var(--paper);
  }
  .cover {
    position: relative;
    width: 849px;
    height: 1200px;
    background: var(--paper);
    overflow: hidden;
  }
  .school-name {
    position: absolute;
    left: 82px;
    top: 96px;
    width: 240px;
    font-family: "Barlow", sans-serif;
    font-weight: 500;
    font-size: 26px;
    line-height: 29px;
    color: var(--brand-blue);
  }
  .company-name {
    position: absolute;
    right: 66px;
    top: 92px;
    display: flex;
    align-items: center;
    gap: 12px;
    font-family: "Barlow", sans-serif;
    font-weight: 500;
    font-size: 30px;
    letter-spacing: 1px;
    color: var(--brand-blue);
  }
  .company-name .mark {
    width: 30px;
    height: 30px;
    background: var(--brand-blue);
  }
  .thesis-kind {
    position: absolute;
    left: 0;
    top: 344px;
    width: 100%;
    margin: 0;
    text-align: center;
    font-family: "Barlow", sans-serif;
    font-weight: 400;
    font-size: 19px;
    line-height: 22px;
    letter-spacing: 2px;
    color: var(--muted-grey);
  }
  .thesis-title {
    position: absolute;
    left: 82px;
    top: 374px;
    width: 701px;
    margin: 0;
    text-align: center;
    font-family: "Bebas Neue", sans-serif;
    font-weight: 400;
    font-size: 118px;
    line-height: 118px;
    letter-spacing: 1px;
    color: var(--brand-blue);
    white-space: nowrap;
  }
  .subtitle-band {
    position: absolute;
    left: 82px;
    top: 494px;
    width: 701px;
    height: 102px;
    background: var(--brand-blue);
    display: flex;
    align-items: center;
    justify-content: center;
    text-align: center;
    font-family: "Barlow", sans-serif;
    font-weight: 300;
    font-size: 27px;
    line-height: 41px;
    letter-spacing: 0.5px;
    color: var(--paper);
  }
  .thesis-details {
    position: absolute;
    left: 228px;
    top: 845px;
    border-collapse: collapse;
  }
  .thesis-details th,
  .thesis-details td {
    padding: 0;
    height: 39.6px;
    vertical-align: middle;
    text-align: left;
  }
  .thesis-details th {
    width: 203px;
    font-family: Verdana, sans-serif;
    font-weight: 400;
    font-size: 12px;
    text-transform: uppercase;
    letter-spacing: 0.3px;
    color: var(--brand-blue);
  }
  .thesis-details td {
    font-family: Verdana, sans-serif;
    font-size: 17px;
    color: var(--ink);
  }
</style>
</head>
<body>
  <main class="cover">
    <div class="school-name">Hochschule<br>Lindenau</div>
    <div class="company-name"><span class="mark"></span>CARDWAVE</div>

    <p class="thesis-kind">MASTER'S THESIS</p>
    <h1 class="thesis-title">MOBILE USABILITY</h1>
    <div class="subtitle-band">Analysis of the mobile<br>application portfolio of XXXXX Ltd</div>

    <table class="thesis-details">
      <tr><th>Name and Surname</th><td>Torben Reimann</td></tr>
      <tr><th>Matriculation Number</th><td>000XXXXX</td></tr>
      <tr><th>Degree Program</th><td>Marketing/Sales/Media</td></tr>
      <tr><th>Issued On</th><td>06.11.2013</td></tr>
      <tr><th>Submitted On</th><td>07.04.2014</td></tr>
      <tr><th>First Examiner</th><td>Prof. Dr. Anton Keller</td></tr>
      <tr><th>Second Examiner</th><td>Prof. Dr. Lukas Brandt</td></tr>
    </table>
  </main>
</body>
</html>
```